Rebrand stationary with recently completed logo design

Need new business cards, thank you cards, letterhead, envelopes and presentation folders. The designs will be sent to a separate production firm so I need the files to be print ready.

My contact info
Reno Vasquell

Office 604-381-5047
Fax 604-317-4860

Email reno@glazemark.ca
website www.glazemark.ca

315-20740 47th Avenue,
Langley, BC, V2K 3P8

Target Market(s)

Homeowners, businesses and contractors

Industry/Entity Type

Business

Font styles to use
Sans Serif

Colors
34a7d7

Requirements
Must have
• Like to have one side of the business card a solid color with the logo in all white. The side with all the text to be a white background
• I find the current blue on the front of the card with the white logo too dark.
Should not have
• Gradient colors

```html
<!DOCTYPE html>
<html lang="en">
<head>
<meta charset="utf-8">
<title>Glazemark – With Compliments Slip</title>
<link rel="stylesheet" href="https://fonts.googleapis.com/css2?family=Open+Sans:wght@300;400&display=swap">
<style>
  :root {
    --brand-blue: #4ccfef;
    --brand-dark: #2b3436;
    --paper: #ffffff;
    --type-light: #ffffff;
  }
  html, body {
    margin: 0;
    padding: 0;
    width: 1200px;
    height: 583px;
    overflow: hidden;
    background: var(--paper);
  }
  .slip {
    position: relative;
    width: 1200px;
    height: 583px;
    overflow: hidden;
    background: var(--paper);
    font-family: "Open Sans", sans-serif;
  }
  .edge-bar {
    position: absolute;
    left: 0;
    top: 0;
    width: 24px;
    height: 583px;
    background: var(--brand-blue);
  }
  .edge-rule {
    position: absolute;
    left: 32px;
    top: 0;
    width: 4px;
    height: 583px;
    background: var(--brand-dark);
  }
  .brand-name {
    position: absolute;
    left: 144px;
    top: 92px;
    margin: 0;
    font-size: 44px;
    font-weight: 400;
    letter-spacing: 1px;
    color: var(--brand-blue);
    line-height: 1;
  }
  .slip__title {
    position: absolute;
    left: 789px;
    top: 114px;
    margin: 0;
    font-size: 36px;
    font-weight: 400;
    color: var(--brand-blue);
    line-height: 1;
  }
  .contact-band {
    position: absolute;
    left: 0;
    top: 405px;
    width: 1200px;
    height: 124px;
    box-sizing: border-box;
    background: var(--brand-blue);
    border-top: 6px solid var(--brand-dark);
    border-bottom: 6px solid var(--brand-dark);
  }
  .contact-band__divider {
    position: absolute;
    top: 16px;
    width: 2px;
    height: 93px;
    background: var(--type-light);
  }
  .contact-item {
    position: absolute;
    display: flex;
    align-items: flex-start;
    color: var(--type-light);
    font-size: 17.5px;
    font-weight: 300;
    line-height: 23px;
  }
  .contact-item__icon {
    flex: none;
    width: 32px;
    height: 32px;
    margin-right: 12px;
    margin-top: -5px;
  }
  .contact-item__text { margin: 0; font-style: normal; }
</style>
</head>
<body>
<main class="slip">
  <div class="edge-bar" aria-hidden="true"></div>
  <div class="edge-rule" aria-hidden="true"></div>

  <h1 class="brand-name">GLAZEMARK</h1>
  <p class="slip__title">With Compliments</p>

  <section class="contact-band">
    <div class="contact-item" style="left:204px; top:30px;">
      <svg class="contact-item__icon" viewBox="0 0 30 30" aria-hidden="true">
        <circle cx="15" cy="15" r="13.5" fill="none" stroke="#fff" stroke-width="1.5"/>
        <rect x="8" y="10" width="14" height="10" fill="none" stroke="#fff" stroke-width="1.3"/>
        <path d="M8,10 L15,16 L22,10" fill="none" stroke="#fff" stroke-width="1.3"/>
      </svg>
      <address class="contact-item__text">315-20740 47th Avenue,<br>Langley, BC,<br>V2K 3P8</address>
    </div>

    <div class="contact-band__divider" style="left:483px;"></div>

    <div class="contact-item" style="left:525px; top:28px;">
      <svg class="contact-item__icon" viewBox="0 0 30 30" aria-hidden="true">
        <circle cx="15" cy="15" r="13.5" fill="none" stroke="#fff" stroke-width="1.5"/>
        <text x="15" y="20.5" text-anchor="middle" font-size="16" fill="#fff" font-family="Open Sans, sans-serif">@</text>
      </svg>
      <p class="contact-item__text">reno@glazemark.ca</p>
    </div>
    <div class="contact-item" style="left:525px; top:70px;">
      <svg class="contact-item__icon" viewBox="0 0 30 30" aria-hidden="true">
        <circle cx="15" cy="15" r="13.5" fill="none" stroke="#fff" stroke-width="1.5"/>
        <circle cx="15" cy="15" r="8" fill="none" stroke="#fff" stroke-width="1.2"/>
        <ellipse cx="15" cy="15" rx="3.5" ry="8" fill="none" stroke="#fff" stroke-width="1.2"/>
        <path d="M7,15 H23 M8.5,11 H21.5 M8.5,19 H21.5" stroke="#fff" stroke-width="1"/>
      </svg>
      <p class="contact-item__text">www.glazemark.ca</p>
    </div>

    <div class="contact-band__divider" style="left:779px;"></div>

    <div class="contact-item" style="left:821px; top:28px;">
      <svg class="contact-item__icon" viewBox="0 0 30 30" aria-hidden="true">
        <circle cx="15" cy="15" r="13.5" fill="none" stroke="#fff" stroke-width="1.5"/>
        <path d="M7,9 h10 a2,2 0 0 1 2,2 v4 a2,2 0 0 1 -2,2 h-6 l-3,3 v-3 a2,2 0 0 1 -1,-2 v-4 a2,2 0 0 1 0,-2 z" fill="none" stroke="#fff" stroke-width="1.1"/>
        <path d="M13,18 v1 a2,2 0 0 0 2,2 h5 l3,2.5 v-2.5 a2,2 0 0 0 1,-2 v-4 a2,2 0 0 0 -2,-2 h-3" fill="none" stroke="#fff" stroke-width="1.1"/>
      </svg>
      <p class="contact-item__text">604-381-5047</p>
    </div>
    <div class="contact-item" style="left:821px; top:70px;">
      <svg class="contact-item__icon" viewBox="0 0 30 30" aria-hidden="true">
        <circle cx="15" cy="15" r="13.5" fill="none" stroke="#fff" stroke-width="1.5"/>
        <rect x="10.5" y="7.5" width="9" height="5" fill="none" stroke="#fff" stroke-width="1.1"/>
        <rect x="7.5" y="12.5" width="15" height="7" rx="1" fill="none" stroke="#fff" stroke-width="1.1"/>
        <rect x="10.5" y="17" width="9" height="6" fill="none" stroke="#fff" stroke-width="1.1"/>
      </svg>
      <p class="contact-item__text">604-317-4860</p>
    </div>
  </section>
</main>
</body>
</html>
```